Marlow Filing Desk

We need one (1) unique homepage and five (5) interior pages. We will guarantee this project if the early submissions look promising.
Updates

Project Deadline Extended
Reason: We want to make sure that everyone who wants to submit a design has the time to do so, and to make revisions if necessary. Thanks.

Take a look at sites like http://www.quillnorth.com/, or http://brevo.com/ for some of the sleek, uncluttered design sensibilities we are looking for. Thanks.

Target Market(s)

Men and women who earn under $50,000 a year.

Industry/Entity Type

Interior

Requirements
Must have
• Logo prominently displayed
Tagline: "Affordable Expertise. Only $249."
Call to action button: "Order Now"
Five line, two column chart comparing us to our competitors
Live chat icon
Social media icons
Zentapay, Orla, QR, Ferro, Halvester, Pexbridge Till
Top-level navigation (home, our process, order now, contact, FAQ)
Login (email, password)
Nice to have
• Rotating flash banner for brief quotations or stock photos
Should not have
• We don't like a lot of busy images and colors. One bold color with a few accents here and there is what we prefer. Look to a site like www.tiltgrid.com, www.feltmundrow.com (mostly the landing page is what we like), www.pondlark.com and www.vunel.com.

```html
<!DOCTYPE html>
<html lang="en">
<head>
<meta charset="utf-8">
<title>Harbor Decree Docs</title>
<link href="https://fonts.googleapis.com/css2?family=Ubuntu:wght@400;500;700&display=swap" rel="stylesheet">
<style>
:root{
  --blue:#2f6aa3;
  --blue-dark:#1f4670;
  --blue-head:#2a6aaa;
  --link:#1b5fa8;
  --orange:#f08a1c;
  --orange-dark:#d8690a;
  --ink:#1f2d3d;
  --body:#555;
  --red:#c8302a;
  --cell-a:#d7e2f0;
  --cell-b:#aac1e1;
  --cell-head:#4a7ebf;
  --footer:#1b283b;
  --page:#efefef;
}
*{margin:0;padding:0;box-sizing:border-box}
html,body{width:987px;height:1200px;overflow:hidden;background:var(--page)}
body{font-family:"Ubuntu",sans-serif}
.page{position:relative;width:1200px;height:1459px;transform:scale(0.8225);transform-origin:0 0}

.site-header{position:absolute;left:0;top:0;width:1200px;height:51px;background:#fff;border-bottom:1px solid #cfd6de}
.brand{position:absolute;left:137px;top:12px;display:flex;align-items:center;gap:7px;font-size:21px;font-weight:500;color:var(--link);white-space:nowrap}
.brand-mark{width:24px;height:24px;border:3px solid var(--link);border-radius:3px;flex:none}
.main-nav{position:absolute;left:400px;top:23px;display:flex;font-size:13.5px;font-weight:500;color:#222;white-space:nowrap}
.main-nav span{margin-right:28px}
.utility-nav{position:absolute;left:832px;top:23px;display:flex;align-items:center;font-size:12px;color:var(--link);white-space:nowrap}
.utility-nav .sep{margin:0 13px}
.chat-icon{margin-right:4px}

.hero{position:absolute;left:0;top:51px;width:1200px;height:654px;background:radial-gradient(ellipse 420px 260px at 600px 120px,#4d89c2 0%,var(--blue) 70%,#2b6298 100%)}
.hero-badge{position:absolute;left:537px;top:8px;width:120px;height:120px;border:3px solid #fff;border-radius:50%;display:flex;align-items:center;justify-content:center;text-align:center;color:#fff;font-size:17px;font-weight:500;line-height:1.2}
.tagline{position:absolute;left:0;top:146px;width:1200px;text-align:center;font-size:30px;font-weight:500;color:#fff;letter-spacing:.5px}
.tagline .soft{color:#e3eef8}
.order-btn{position:absolute;left:498px;top:208px;width:197px;height:54px;border-radius:6px;background:linear-gradient(#f7a23a,var(--orange) 55%,var(--orange-dark));color:#fff;font-size:24px;font-weight:700;text-align:center;line-height:54px;box-shadow:0 3px 6px rgba(0,0,0,.25)}
.slider-frame{position:absolute;left:228px;top:302px;width:750px;height:352px;border:1px solid #7fc3e6;background:#f2f2f2;overflow:hidden}
.slide-art{position:absolute;inset:0;background:linear-gradient(160deg,#e9e9e9 0%,#cfcfcf 35%,#f5f5f5 60%,#e4efd6 100%)}
.slide-title{position:absolute;left:0;top:166px;width:100%;text-align:center;font-size:46px;color:#1e466f;padding-left:30px}
.arrow{position:absolute;top:474px}

.caption-bar{position:absolute;left:0;top:705px;width:1200px;height:40px;background:linear-gradient(#2a527c,var(--blue-dark));color:#fff;text-align:center;line-height:40px;font-size:16px}
.caption-pointer{position:absolute;left:589px;top:744px}

.headline{position:absolute;left:0;top:756px;width:1200px;text-align:center;font-size:50px;font-weight:700;color:var(--blue-head)}
.section-title{font-size:16px;font-weight:500;color:var(--ink)}
.welcome{position:absolute;left:184px;top:831px;width:551px}
.welcome p{margin-top:6px;font-size:11.8px;line-height:18px;color:var(--body);letter-spacing:-.1px}
.read-more{display:block;text-align:right;margin-top:6px;font-size:12.5px;font-weight:500;color:var(--red)}
.rule{position:absolute;height:1px;background:#d0d0d0}
.testimonial{position:absolute;left:770px;top:831px;width:255px}
.testimonial p{margin-top:8px;font-size:12.5px;line-height:18px;color:var(--body)}
.testimonial .cite{text-align:right;font-style:italic;color:var(--red);font-size:12.5px;line-height:16px}

.compare-title{position:absolute;left:185px;top:977px}
.compare{position:absolute;left:182px;top:1003px;border-collapse:separate;border-spacing:4px 3px}
.compare td,.compare th{height:29px;text-align:center;font-size:13.5px;font-weight:400}
.compare th{background:var(--cell-head);color:#fff}
.compare .row-head{width:158px;background:var(--cell-head);color:#fff}
.compare .mark{width:187px;color:#1f2d3d;font-size:18px;font-weight:700}
.compare tr.odd .mark{background:var(--cell-a)}
.compare tr.even .mark{background:var(--cell-b)}

.payments-title{position:absolute;left:770px;top:978px}
.pay{position:absolute;width:60px;height:37px;border:1px solid #c9d2dc;border-radius:3px;background:#fff;display:flex;align-items:center;justify-content:center;font-size:10px;font-weight:500;color:var(--link);text-align:center;line-height:1.1}
.social-title{position:absolute;left:770px;top:1147px}
.social{position:absolute;width:36px;height:36px;border-radius:5px;background:var(--link);color:#fff;font-size:8px;display:flex;align-items:center;justify-content:center}

.site-footer{position:absolute;left:0;top:1337px;width:1200px;height:122px;background:linear-gradient(#223350,var(--footer))}
.footer-nav{position:absolute;left:292px;top:19px;display:flex;font-size:12.5px;font-weight:500;color:#fff;white-space:nowrap}
.footer-nav .sep{margin:0 26px}
.footer-brand{position:absolute;left:0;width:1200px;top:58px;display:flex;justify-content:center;align-items:center;gap:7px;font-size:20px;font-weight:500;color:#8d96a3}
.footer-brand .brand-mark{width:20px;height:20px;border:2px solid #8d96a3}
.copyright{position:absolute;left:0;top:98px;width:1200px;text-align:center;font-size:11.5px;color:#c7ced8}
</style>
</head>
<body>
<div class="page">

  <header class="site-header">
    <div class="brand"><span class="brand-mark"></span>Harbor Decree Docs</div>
    <nav class="main-nav">
      <span>HOME</span><span>ABOUT US</span><span>OUR PROCESS</span><span>FAQ</span><span>ORDER NOW</span>
    </nav>
    <div class="utility-nav">
      <svg class="chat-icon" width="18" height="16" viewBox="0 0 18 16"><path d="M2 1h14a1 1 0 0 1 1 1v8a1 1 0 0 1-1 1H8l-4 4v-4H2a1 1 0 0 1-1-1V2a1 1 0 0 1 1-1z" fill="#2a78c8"/></svg>
      <span>Live Chat</span><span class="sep">|</span><span>User Login</span><span class="sep">|</span><span>Contact Us</span>
    </div>
  </header>

  <section class="hero">
    <div class="hero-badge">Marlow<br>Filing Desk</div>
    <div class="tagline">Affordable Expertise. <span class="soft">Only $249.</span></div>
    <div class="order-btn">ORDER NOW</div>

    <div class="slider-frame">
      <div class="slide-art" role="img" aria-label="Rotating banner image of a website preview"></div>
      <div class="slide-title">Slide Images Goes Here</div>
    </div>
    <svg class="arrow" style="left:199px" width="20" height="40" viewBox="0 0 20 40"><path d="M20 0v40L0 20z" fill="var(--orange)"/></svg>
    <svg class="arrow" style="left:991px" width="20" height="40" viewBox="0 0 20 40"><path d="M0 0v40l20-20z" fill="var(--orange)"/></svg>
  </section>

  <div class="caption-bar">Demo text goes here</div>
  <svg class="caption-pointer" width="22" height="13" viewBox="0 0 22 13"><path d="M0 0h22L11 13z" fill="var(--blue-dark)"/></svg>

  <h1 class="headline">Get Everything You Need in Divorce</h1>

  <div class="welcome">
    <h2 class="section-title">Welcome to Harbor Decree Docs</h2>
    <p>Lorem ipsum dolor sit amet, consectetur adipisicing elit, sed do eiusmod tempor incididunt ut labore et dolore magna aliqua. Ut enim ad minim veniam, quis nostrud exercitation ullamco laboris nisi ut aliquip ex ea commodo consequat. Duis aute irure dolor in reprehenderit in voluptate velit esse cillum</p>
    <span class="read-more">Read More</span>
  </div>
  <div class="rule" style="left:184px;top:937px;width:551px"></div>

  <div class="testimonial">
    <h2 class="section-title">Client Testimonials</h2>
    <p>“Lorem ipsum dolor sit amet, consectetur adipminim veniam, quis nostrud exercitation minim veniam minim veniamminim veniam”</p>
    <div class="cite">Madison, www.quoteline.com</div>
  </div>
  <div class="rule" style="left:770px;top:937px;width:255px"></div>

  <h2 class="section-title compare-title">Welcome to Harbor Decree Docs</h2>
  <table class="compare">
    <tr><th style="width:158px">Text Heading</th><th style="width:187px">Text Heading - 1</th><th style="width:187px">Text Heading - 2</th></tr>
    <tr class="odd"><td class="row-head">Text Heading</td><td class="mark">✔</td><td class="mark">✔</td></tr>
    <tr class="even"><td class="row-head">Text Heading</td><td class="mark">✔</td><td class="mark">✔</td></tr>
    <tr class="odd"><td class="row-head">Text Heading</td><td class="mark">✔</td><td class="mark">✔</td></tr>
    <tr class="even"><td class="row-head">Text Heading</td><td class="mark">✔</td><td class="mark">✔</td></tr>
    <tr class="odd"><td class="row-head">Text Heading</td><td class="mark">X</td><td class="mark">X</td></tr>
    <tr class="even"><td class="row-head">Text Heading</td><td class="mark">✔</td><td class="mark">X</td></tr>
    <tr class="odd"><td class="row-head">Text Heading</td><td class="mark">✔</td><td class="mark">X</td></tr>
    <tr class="even"><td class="row-head">Text Heading</td><td class="mark">✔</td><td class="mark">X</td></tr>
    <tr class="odd"><td class="row-head">Text Heading</td><td class="mark">X</td><td class="mark">X</td></tr>
  </table>

  <h2 class="section-title payments-title">Our Payment Options</h2>
  <div class="pay" style="left:774px;top:1007px">Zentapay</div>
  <div class="pay" style="left:847px;top:1007px">Halvester</div>
  <div class="pay" style="left:920px;top:1007px">Pexbridge Till</div>
  <div class="pay" style="left:774px;top:1057px">Orla</div>
  <div class="pay" style="left:847px;top:1057px">Ferro</div>
  <div class="pay" style="left:920px;top:1057px">QR</div>
  <div class="rule" style="left:770px;top:1127px;width:255px"></div>

  <h2 class="section-title social-title">Our Social Network</h2>
  <div class="social" style="left:770px;top:1177px">Folkly</div>
  <div class="social" style="left:822px;top:1177px">Chirpo</div>
  <div class="social" style="left:873px;top:1177px">Linkwell</div>
  <div class="social" style="left:924px;top:1177px">Tumbo</div>
  <div class="social" style="left:974px;top:1177px">Savory</div>
  <div class="social" style="left:770px;top:1228px">Skyvo</div>
  <div class="social" style="left:822px;top:1228px">Flashy</div>
  <div class="social" style="left:873px;top:1228px">Feed</div>
  <div class="social" style="left:924px;top:1228px">Mynook</div>
  <div class="social" style="left:974px;top:1228px">Gobo</div>

  <footer class="site-footer">
    <nav class="footer-nav">
      <span>Home</span><span class="sep">|</span><span>About Us</span><span class="sep">|</span><span>Pricing</span><span class="sep">|</span><span>Our Process</span><span class="sep">|</span><span>Client login</span><span class="sep">|</span><span>Contact Us</span>
    </nav>
    <div class="footer-brand"><span class="brand-mark"></span>Harbor Decree Docs</div>
    <div class="copyright">2011-2012 HarborDecreeDocs</div>
  </footer>

</div>
</body>
</html>
```